Poster Design job - 11"x17" Poster for a Treasure Hunt

Summary:This project is for a poster that will be used to promote a community treasure hunt for kids aged 9-14. This will be the 14th year we have put on the treasure hunt. See the files for previous posters we have used (all from PixelBazaar).***Please thoroughly read below before embarking on this project.We loved everything about the 2012 design, particularly how all of the elements seem to belong exactly where they are on the poster. Previous years designs just had text blocks thrown on top of a background image which doesn't make a for a good poster; if within a few seconds you don’t have an idea about what even the poster is promoting, and if you can’t read every part of the poster from 6 feet away, the poster isn't working. Some of our other favorite posters for you to see are from 2012, 2016, and 2017, 2018(attached).Please make the Ridgewell Loot Seekers logo a featured part of the design. See the 2012 poster winner where the logo was centered right at the top and very prominent.Style: Scary, but remember the event is for children 9-14years old. The title of the hunt this year is "The Shivering Story of Hollis Merton".The main character in our poster is the spirit of an old man named Hollis Merton. His soul wanders in search of someone. I want the spirit to look like the figure of an old man, dark, spooky, but not too scary and you cannot clearly see his face. - the time period is the 1970s- Use the attached picture of the building as a reference in the background attached as a starting point. That pic is only meant as a reference. Do not copy this pic direclty as there are probably copyrights on it so please make changes to the picture.- Place the scary old man figure centered in the poster so its clear he is a central character. Poster must contain these texts:event name: "The Shivering Story of Hollis Merton""Be the First Team to unravel the mystery of the Hollis Merton and you will find a hidden Treasure chest and claim a FANTASTIC PRIZE!""Youth Ages 9-14 are able to participate."Team Applications are available on Sept 1st and due ASAP""Space is limited to the first 50 teams""Presented by Dr. Owen Pirtle of Bellmont Orthodontics""WWW.RWLOOTSEEKERS.COM"**Must include on the poster the logo of Bellmont Orthodontics, and Ridgewell Loot Seekers, event date of oct 12 2019. _____Remember, we want scary, but NOT gross and gruesome as this is for kids 9-14. Some of the poster submissions from previous years were way too gruesome with blood and gore. Do keep in mind this event is for children. For good examples, see the previous years posters attached.

```html
<!DOCTYPE html>
<html lang="en">
<head>
<meta charset="utf-8">
<title>The Shivering Story of Hollis Merton – Poster</title>
<link href="https://fonts.googleapis.com/css2?family=Almendra+SC&family=Creepster&family=Luckiest+Guy&display=swap" rel="stylesheet">
<style>
  :root{
    --page:#e9e4dc;
    --ink-dark:#0d0806;
    --sky-top:#2a0d08;
    --sky-mid:#5b2a1c;
    --moon:#b58aa6;
    --white:#f7f3ec;
    --yellow:#ffe23a;
    --orange:#ff9a12;
    --deep-orange:#f26a06;
    --gold:#e8b62a;
  }
  *{margin:0;padding:0;box-sizing:border-box}
  html,body{width:1200px;height:1200px;overflow:hidden;background:var(--page)}
  .poster{
    position:absolute;left:230px;top:45px;width:740px;height:1110px;
    background:linear-gradient(180deg,var(--sky-top) 0%,var(--sky-mid) 38%,#3a1a1a 60%,var(--ink-dark) 82%);
    overflow:hidden;
    font-family:"Luckiest Guy",cursive;
    color:var(--white);
  }
  h1{font-size:inherit;font-weight:normal}
  .night-scene{position:absolute;left:0;top:0;width:740px;height:1110px}
  .spirit-figure{position:absolute;left:452px;top:455px;width:160px;height:530px}
  .abs{position:absolute;white-space:nowrap;line-height:1}
  .hunt-logo{left:60px;width:440px;top:96px;text-align:center;
    font-family:"Almendra SC",serif;font-size:30px;color:var(--gold);letter-spacing:1px}
  .hunt-logo .dot{display:inline-block;width:12px;height:12px;border-radius:50%;background:var(--gold);margin-right:10px;vertical-align:middle}
  .ortho-logo{left:560px;top:36px;width:170px;text-align:center;
    font-family:"Almendra SC",serif;font-size:20px;line-height:1.15;color:var(--white)}
  .ortho-logo .mark{display:block;width:34px;height:34px;border:3px solid var(--white);border-radius:50%;margin:0 auto 8px}
  .title-lead{left:0;width:740px;top:232px;text-align:center;
    font-family:"Almendra SC",serif;font-size:42px;color:var(--orange);letter-spacing:1px}
  .title-name{left:0;width:740px;top:282px;text-align:center;
    font-family:"Creepster",cursive;font-size:92px;
    background:linear-gradient(180deg,var(--yellow) 15%,var(--orange) 55%,var(--deep-orange) 90%);
    -webkit-background-clip:text;background-clip:text;color:transparent}
  .event-date{left:170px;width:260px;top:384px;text-align:center;
    font-family:"Almendra SC",serif;font-size:40px;color:var(--orange)}
  .intro{left:24px;top:450px;font-size:22px;line-height:27px}
  .intro-name{left:24px;top:512px;font-size:50px;color:var(--yellow)}
  .prize{left:24px;top:580px;font-size:26px;line-height:33px;color:var(--orange)}
  .prize .yellow{color:var(--yellow)}
  .ages{left:24px;top:748px;font-size:42px}
  .ages .num{color:var(--yellow)}
  .ages-sub{left:24px;top:798px;font-size:28px}
  .apply{left:24px;top:856px;font-size:21px}
  .apply-date{left:24px;top:888px;font-size:36px;color:var(--yellow)}
  .limit{left:588px;top:750px;width:148px;text-align:center;font-size:20px;line-height:27px}
  .limit-num{left:588px;top:838px;width:148px;text-align:center;font-size:56px;color:var(--orange)}
  .limit-unit{left:588px;top:896px;width:148px;text-align:center;font-size:28px;color:var(--orange)}
  .presented{left:0;width:740px;top:990px;text-align:center;font-size:12.5px;letter-spacing:0.5px}
  .presented .yellow{color:var(--yellow)}
  .site{left:0;width:740px;top:1016px;text-align:center;font-size:32px;color:var(--orange);letter-spacing:1px}
</style>
</head>
<body>
<main class="poster">
  <svg class="night-scene" viewBox="0 0 740 1110" role="img" aria-label="Night sky with a full moon, flying bats, ink splatter, bare trees, graveyard grass and a haunted house">
    <defs>
      <radialGradient id="moonGlow" cx="0.42" cy="0.52" r="0.42">
        <stop offset="0" stop-color="#b58aa6"/>
        <stop offset="0.45" stop-color="#8a5a6e" stop-opacity="0.85"/>
        <stop offset="1" stop-color="#3a1a1a" stop-opacity="0"/>
      </radialGradient>
      <linearGradient id="ground" x1="0" y1="0" x2="0" y2="1">
        <stop offset="0" stop-color="#0d0806" stop-opacity="0"/>
        <stop offset="1" stop-color="#0d0806"/>
      </linearGradient>
    </defs>
    <rect width="740" height="1110" fill="url(#moonGlow)"/>
    <rect x="0" y="720" width="740" height="390" fill="url(#ground)"/>
  </svg>
  <svg class="spirit-figure" viewBox="0 0 160 530" role="img" aria-label="Dark shadowy figure of an old man in a cap and overalls standing before the house">
    <defs>
      <linearGradient id="figureShade" x1="0" y1="0" x2="0" y2="1">
        <stop offset="0" stop-color="#231c1a"/>
        <stop offset="1" stop-color="#0b0908"/>
      </linearGradient>
    </defs>
    <rect x="0" y="0" width="160" height="530" rx="40" fill="url(#figureShade)"/>
  </svg>

  <div class="abs hunt-logo"><span class="dot"></span>Ridgewell Loot Seekers</div>
  <div class="abs ortho-logo"><span class="mark"></span>Bellmont<br>Orthodontics</div>

  <h1>
    <span class="abs title-lead">The Shivering Story of</span>
    <span class="abs title-name">HOLLIS MERTON</span>
  </h1>
  <div class="abs event-date">12 Oct 2019</div>

  <p class="abs intro">BE THE FIRST TEAM TO<br>UNRAVEL THE MYSTERY OF THE</p>
  <p class="abs intro-name">HOLLIS MERTON</p>
  <p class="abs prize">AND YOU WILL FIND A HIDDEN<br>TREASURE CHEST AND CLAIM A<br><span class="yellow">FANTASTIC PRIZE!</span></p>

  <p class="abs ages">YOUTH AGES <span class="num">9-14</span></p>
  <p class="abs ages-sub">ARE ABLE TO PARTICIPATE</p>

  <p class="abs apply">TEAM APPLICATIONS ARE AVAILABLE ON</p>
  <p class="abs apply-date">SEPT 1ST AND DUE ASAP</p>

  <p class="abs limit">SPACE IS<br>LIMITED TO<br>THE FIRST</p>
  <p class="abs limit-num">50</p>
  <p class="abs limit-unit">TEAMS</p>

  <p class="abs presented">PRESENTED BY <span class="yellow">DR. OWEN PIRTLE</span> OF <span class="yellow">BELLMONT ORTHODONTICS</span></p>
  <p class="abs site">WWW.RWLOOTSEEKERS.COM</p>
</main>
</body>
</html>
```